High Tech Real Estate Startup needs a business card

We are developing an innovative real estate marketing product based around advanced search and virtual reality.

We talk to people, we need business cards.

Target Market(s)

The target market is technology professionals and realtors.

Contact Information for Business Card

The information to be included will include

Name
Title
Phone Number
E-mail Address
www.quelzo.com

It should use simple iconography for each one of those fields.

Font styles to use
Other font styles liked:
• Co, Jubilat, Avenir

Colors

Designer to choose colors to be used in the design.

Requirements
Must have
• Clean aesthetic,
• Good use of negative space.
• It should use our company logo, shown in the attached file. It is able to use the negative of that logo (coloured font and white background) and I have attached other acceptable accent colours in a swatch file.
Should not have
• Should not be too busy
• No extraneous text (slogans, tag lines etc)

```html
<!DOCTYPE html>
<html lang="en">
<head>
<meta charset="utf-8">
<title>Quelzo Business Card</title>
<link rel="stylesheet" href="https://fonts.googleapis.com/css2?family=Montserrat:wght@400;500&family=Open+Sans:wght@400;600&display=swap">
<style>
  :root {
    --teal: #17b4b7;
    --teal-deep: #10a7aa;
    --paper: #f6f6f6;
    --ink: #3a3a3a;
    --ink-soft: #6a6a6a;
    --backdrop: #3b3b3b;
  }
  * { box-sizing: border-box; margin: 0; padding: 0; }
  html, body { width: 1200px; height: 876px; overflow: hidden; }
  body {
    background: var(--backdrop);
    font-family: "Open Sans", Arial, sans-serif;
    position: relative;
  }
  .card {
    position: absolute;
    left: 320px;
    width: 560px;
    height: 320px;
    border-radius: 34px;
    box-shadow: 0 10px 28px rgba(0,0,0,.35);
  }
  .card-front { top: 86px; background: var(--paper); }
  .card-back {
    top: 470px;
    background: linear-gradient(135deg, #1fbcbf 0%, var(--teal) 50%, var(--teal-deep) 100%);
    display: flex; align-items: center; justify-content: center;
  }
  .wordmark {
    font-family: "Montserrat", Arial, sans-serif;
    font-weight: 500;
    letter-spacing: .08em;
  }
  .front-mark {
    position: absolute;
    left: 70px; top: 138px;
    font-size: 34px;
    color: var(--teal);
  }
  .divider {
    position: absolute;
    left: 270px; top: 88px;
    width: 2px; height: 144px;
    background: linear-gradient(to bottom, rgba(90,90,90,0), rgba(70,70,70,.75) 50%, rgba(90,90,90,0));
  }
  .contact { position: absolute; left: 300px; top: 96px; }
  .contact-name {
    font-family: "Montserrat", Arial, sans-serif;
    font-size: 22px; color: var(--teal); line-height: 1.1;
  }
  .contact-role { font-size: 12px; color: var(--ink-soft); margin: 2px 0 14px; }
  .contact-list { list-style: none; }
  .contact-list li {
    display: flex; align-items: center; gap: 10px;
    font-size: 13px; color: var(--ink); line-height: 24px;
  }
  .contact-list svg { width: 13px; height: 13px; flex: none; }
  .back-mark { font-size: 84px; color: #fff; }
</style>
</head>
<body>
  <section class="card card-front">
    <div class="wordmark front-mark">QUELZO</div>
    <div class="divider"></div>
    <div class="contact">
      <p class="contact-name">Nora Kessel</p>
      <p class="contact-role">Nora Kessel</p>
      <ul class="contact-list">
        <li>
          <svg viewBox="0 0 14 14" aria-hidden="true"><rect x="3.5" y="1" width="7" height="12" rx="1.2" fill="none" stroke="var(--teal)" stroke-width="1.4"/><circle cx="7" cy="11" r=".8" fill="var(--teal)"/></svg>
          (+100) 555.0199.200
        </li>
        <li>
          <svg viewBox="0 0 14 14" aria-hidden="true"><rect x="1" y="3" width="12" height="8.5" rx="1" fill="var(--teal)"/><path d="M1.5 3.6 7 8l5.5-4.4" fill="none" stroke="#fff" stroke-width="1.1"/></svg>
          n.kessel@quelzo.com
        </li>
        <li>
          <svg viewBox="0 0 14 14" aria-hidden="true"><circle cx="7" cy="7" r="6" fill="var(--teal)"/><path d="M1 7h12M7 1c-2.4 2.5-2.4 9.5 0 12M7 1c2.4 2.5 2.4 9.5 0 12" fill="none" stroke="#fff" stroke-width=".9"/></svg>
          www.quelzo.com
        </li>
      </ul>
    </div>
  </section>

  <section class="card card-back">
    <div class="wordmark back-mark">QUELZO</div>
  </section>
</body>
</html>
```